依頼詳細
レスポンシブウェブデザインを意識したデザインでお願いします。
参考URL
https://morisato-koubou.jp/

デザインに関しては、添付してあるデザインレイアウトシートを基にお願いします。

まずはパソコンサイトのデザインをお願いします。
当選後、スマホデザインをお願いします。

既存のテンプレートを使う場合は
テンプレート名を下記のような記載を提案の中にいれてください。
例:WordpressテーマはKandoria、デザインスキンは無料のHLM2019 RX4(http://kandoria.com/ex_plugin/hlmnagoya2019_rx4/)をベースにデザインいたしました。
など

素材となる写真は現在、撮影中ですので、一旦他のサイトや参考URLの写真をサンプルとして入れてください。(サンプルなどの表記をお願いします)
また、購入が必要な写真などを利用した場合は、Pelmora Stock(https://stock.pelmora.com/jp/)からファイル番号と価格を教えてください。
ページ数
1ページ
希望イメージ
シンプル 複雑
単色 カラフル
暗い 明るい
日常 高級
遊び心 厳粛
未来的 伝統的
女性的 男性的
希望する色
茶系、緑系
納品ファイル
• イラストレーター形式 (.ai)
• フォトショップ形式 (.psd)
• PNG形式 (.png)
補足説明
上記のいずれか1つ。アウトラインありとなしの2つ。

クライアントのイメージ通りでした。

たくさんのご提案ありがとうございました。
次回もぜひ、よろしくお願い致します。

```html
<!DOCTYPE html>
<html lang="ja">
<head>
<meta charset="utf-8">
<title>株式会社 モリサト</title>
<link href="https://fonts.googleapis.com/css2?family=Noto+Sans+JP:wght@400;500;700&family=Noto+Serif+JP:wght@500;700&display=swap" rel="stylesheet">
<style>
:root{
  --green:#2f9148;
  --green-dark:#1f7a37;
  --green-light:#5cb85c;
  --green-soft:#43a05a;
  --cream:#fbf1e6;
  --beige:#efdfcb;
  --box:#ecdac3;
  --text:#3a3a3a;
  --white:#ffffff;
}
*{margin:0;padding:0;box-sizing:border-box}
html,body{width:1200px;height:5044px;overflow:hidden}
body{font-family:"Noto Sans JP",sans-serif;color:var(--text);background:var(--white);position:relative}
section,header,footer,nav{position:absolute;left:0;width:1200px}
.site-header{top:0;height:56px;background:var(--white)}
.brand{position:absolute;left:72px;top:14px;display:flex;align-items:center;gap:10px;font-size:17px;font-weight:700;color:var(--text)}
.brand-dot{width:26px;height:26px;border-radius:50%;background:var(--green)}
.global-nav{top:56px;height:34px;background:var(--green-soft);display:flex;justify-content:center;gap:0}
.global-nav a{color:var(--white);font-size:12px;text-decoration:none;width:128px;text-align:center;line-height:34px}
.global-nav a.active{background:var(--green-dark)}
.hero{top:90px;height:330px;background:var(--green)}
.hero-photo{position:absolute;right:0;top:0;width:680px;height:330px;background:linear-gradient(120deg,#6c9b63,#a9b98a 45%,#d6cfb0 75%,#8aa77a)}
.hero-copy{position:absolute;left:170px;top:110px;color:var(--white);font-family:"Noto Serif JP",serif;font-size:40px;font-weight:700;line-height:1.5;letter-spacing:4px}
.band-cream{background:var(--cream)}
.band-beige{background:var(--beige)}
.sec-title{position:absolute;left:0;width:1200px;text-align:center}
.sec-title .en{position:relative;display:inline-block;font-family:"Noto Serif JP",serif;font-size:28px;font-weight:700;color:var(--text);z-index:1}
.sec-title .en::before{content:"";position:absolute;left:-22px;top:-14px;width:54px;height:54px;border-radius:50%;background:var(--green-light);opacity:.85;z-index:-1}
.sec-title .ja{display:block;font-size:11px;margin-top:2px}
.advantage{top:420px;height:770px}
.adv-list{position:absolute;top:240px;left:70px;display:flex;gap:27px}
.adv-item{width:192px;text-align:center;font-size:17px;line-height:1.45;font-weight:500}
.adv-photo{height:200px;margin-bottom:18px}
.project{top:1190px;height:460px}
.grid4{position:absolute;left:72px;display:flex;gap:22px}
.col{width:250px}
.proj-tile{height:250px;display:flex;align-items:center;justify-content:center;color:var(--white);font-size:18px;font-weight:500}
.dummy{font-size:11px;line-height:1.75;margin-top:18px;letter-spacing:.5px}
.case{top:1650px;height:660px}
.ph-box{height:240px;background:var(--box)}
.case-title{text-align:center;font-size:18px;font-weight:500;margin-top:22px}
.case .dummy{margin-top:10px}
.news{top:2310px;height:490px}
.news-list{position:absolute;left:300px;top:250px;list-style:none}
.news-list li{display:flex;align-items:center;gap:10px;font-size:11px;height:40px}
.news-date{font-size:11px;width:70px}
.news-tag{background:var(--green);color:var(--white);font-size:10px;padding:2px 8px}
.blog{top:2800px;height:710px}
.blog-date{font-size:11px;margin-top:14px}
.blog-title{font-size:17px;font-weight:700;line-height:1.5;margin-top:4px}
.blog .dummy{margin-top:8px}
.faq{top:3510px;height:820px}
.faq-list{position:absolute;left:340px;top:350px;list-style:none}
.faq-list li{margin-bottom:80px}
.qa{display:flex;align-items:center;gap:12px;font-size:12px;height:48px}
.mark{width:22px;height:22px;border-radius:50%;color:var(--white);font-size:11px;text-align:center;line-height:22px;font-weight:700}
.mark.q{background:#6a8fd6}
.mark.a{background:#e07a7a}
.contact{top:4330px;height:225px;background:var(--white)}
.tree{position:absolute;right:0;top:4130px;width:320px;height:425px}
.contact-btn{position:absolute;left:335px;top:112px;width:530px;height:82px;background:var(--green);color:var(--white);font-size:22px;font-weight:500;display:flex;align-items:center;justify-content:center;text-decoration:none}
.site-footer{top:4555px;height:330px;background:var(--green)}
.foot-links{position:absolute;left:0;width:1200px;top:30px;text-align:center;color:var(--white);font-size:11px;line-height:2.4}
.foot-links span{margin:0 6px}
.foot-brand{position:absolute;left:0;width:1200px;top:200px;display:flex;justify-content:center;align-items:center;gap:10px;color:var(--white);font-size:16px;font-weight:700}
.foot-brand .brand-dot{background:var(--white)}
.foot-base{position:absolute;left:0;bottom:0;width:1200px;height:40px;background:var(--green-dark)}
</style>
</head>
<body>
<header class="site-header">
  <div class="brand"><span class="brand-dot"></span>株式会社 モリサト</div>
</header>
<nav class="global-nav">
  <a class="active" href="#">Home</a><a href="#">弊社の強み</a><a href="#">事業案内</a><a href="#">加工事例・商品紹介</a><a href="#">お知らせ</a><a href="#">よくある質問</a><a href="#">お問い合わせ</a>
</nav>
<section class="hero">
  <div class="hero-photo" role="img" aria-label="木材を加工する作業の写真"></div>
  <h1 class="hero-copy">地球にやさしい<br>環境を目指して</h1>
</section>

<section class="advantage band-cream">
  <h2 class="sec-title" style="top:140px"><span class="en">Advantage</span><span class="ja">弊社の強み</span></h2>
  <div class="adv-list">
    <div class="adv-item"><div class="adv-photo" role="img" aria-label="住宅の木造骨組みの写真" style="background:linear-gradient(160deg,#d9c3a0,#9a7a52)"></div>住宅部材<br>加工・戴立</div>
    <div class="adv-item"><div class="adv-photo" role="img" aria-label="丸ノコで木材を切断する写真" style="background:linear-gradient(160deg,#8a8078,#c7ad88)"></div>産業機器<br>(ショーケース)<br>部材加工・戴立</div>
    <div class="adv-item"><div class="adv-photo" role="img" aria-label="木製の床板の写真" style="background:linear-gradient(160deg,#b99a74,#7a5a3c)"></div>床暖<br>パネル加工</div>
    <div class="adv-item"><div class="adv-photo" role="img" aria-label="木製パレットの写真" style="background:linear-gradient(160deg,#e4d0ae,#b69870)"></div>梱包製品<br>梱包請負</div>
    <div class="adv-item"><div class="adv-photo" role="img" aria-label="積まれた木材の写真" style="background:linear-gradient(160deg,#ead6b4,#c4a27a)"></div>その他<br>加工処理</div>
  </div>
</section>

<section class="project band-cream">
  <h2 class="sec-title" style="top:32px"><span class="en">Project</span><span class="ja">事業案内</span></h2>
  <div class="grid4" style="top:140px">
    <div class="col"><div class="proj-tile" role="img" aria-label="材料の木材写真に緑の重ね" style="background:linear-gradient(150deg,#3f9a52,#2b7f40)">材料</div><p class="dummy">テキストテキストテキストテキストテキストテキストテキストテキストテキストテキストテキストテキストテキストテキストテキストテキスト</p></div>
    <div class="col"><div class="proj-tile" role="img" aria-label="加工・戴立の写真に緑の重ね" style="background:linear-gradient(150deg,#49a35a,#2d8442)">加工･戴立</div><p class="dummy">テキストテキストテキストテキストテキストテキストテキストテキストテキストテキストテキストテキストテキストテキストテキストテキスト</p></div>
    <div class="col"><div class="proj-tile" role="img" aria-label="設備の写真に緑の重ね" style="background:linear-gradient(150deg,#3a9450,#26783b)">設備</div><p class="dummy">テキストテキストテキストテキストテキストテキストテキストテキストテキストテキストテキストテキストテキストテキストテキストテキスト</p></div>
    <div class="col"><div class="proj-tile" role="img" aria-label="丸太の断面写真に緑の重ね" style="background:linear-gradient(150deg,#4ba55c,#30884a)">オーダーメイド</div><p class="dummy">テキストテキストテキストテキストテキストテキストテキストテキストテキストテキストテキストテキストテキストテキストテキストテキスト</p></div>
  </div>
</section>

<section class="case band-cream">
  <h2 class="sec-title" style="top:52px"><span class="en">Case</span><span class="ja">加工事例・商品紹介</span></h2>
  <div class="grid4" style="top:160px">
    <div class="col"><div class="ph-box" role="img" aria-label="加工事例の写真"></div><h3 class="case-title">タイトル</h3><p class="dummy">テキストテキストテキストテキストテキストテキストテキストテキストテキストテキストテキストテキストテキストテキストテキストテキスト</p></div>
    <div class="col"><div class="ph-box" role="img" aria-label="加工事例の写真"></div><h3 class="case-title">タイトル</h3><p class="dummy">テキストテキストテキストテキストテキストテキストテキストテキストテキストテキストテキストテキストテキストテキストテキストテキスト</p></div>
    <div class="col"><div class="ph-box" role="img" aria-label="加工事例の写真"></div><h3 class="case-title">タイトル</h3><p class="dummy">テキストテキストテキストテキストテキストテキストテキストテキストテキストテキストテキストテキストテキストテキストテキストテキスト</p></div>
    <div class="col"><div class="ph-box" role="img" aria-label="加工事例の写真"></div><h3 class="case-title">タイトル</h3><p class="dummy">テキストテキストテキストテキストテキストテキストテキストテキストテキストテキストテキストテキストテキストテキストテキストテキスト</p></div>
  </div>
</section>

<section class="news band-beige">
  <h2 class="sec-title" style="top:140px"><span class="en">News</span><span class="ja">お知らせ</span></h2>
  <ul class="news-list">
    <li><span class="news-date">2020.01.01</span><span class="news-tag">お知らせ</span>テキストテキストテキストテキストテキストテキストテキストテキストテキストテキストテキスト</li>
    <li><span class="news-date">2020.01.01</span><span class="news-tag">お知らせ</span>テキストテキストテキストテキストテキストテキストテキストテキストテキストテキストテキスト</li>
    <li><span class="news-date">2020.01.01</span><span class="news-tag">お知らせ</span>テキストテキストテキストテキストテキストテキストテキストテキストテキストテキストテキスト</li>
  </ul>
</section>

<section class="blog band-cream">
  <h2 class="sec-title" style="top:130px"><span class="en">Blog</span><span class="ja">ブログ</span></h2>
  <div class="grid4" style="top:242px">
    <div class="col"><div class="ph-box" role="img" aria-label="ブログ記事の写真"></div><p class="blog-date">2020.01.01</p><h3 class="blog-title">タイトルタイトルタイトル<br>タイトルタイトル</h3><p class="dummy">テキストテキストテキストテキストテキストテキストテキストテキストテキストテキストテキストテキスト</p></div>
    <div class="col"><div class="ph-box" role="img" aria-label="ブログ記事の写真"></div><p class="blog-date">2020.01.01</p><h3 class="blog-title">タイトルタイトルタイトル<br>タイトルタイトル</h3><p class="dummy">テキストテキストテキストテキストテキストテキストテキストテキストテキストテキストテキストテキスト</p></div>
    <div class="col"><div class="ph-box" role="img" aria-label="ブログ記事の写真"></div><p class="blog-date">2020.01.01</p><h3 class="blog-title">タイトルタイトルタイトル<br>タイトルタイトル</h3><p class="dummy">テキストテキストテキストテキストテキストテキストテキストテキストテキストテキストテキストテキスト</p></div>
    <div class="col"><div class="ph-box" role="img" aria-label="ブログ記事の写真"></div><p class="blog-date">2020.01.01</p><h3 class="blog-title">タイトルタイトルタイトル<br>タイトルタイトル</h3><p class="dummy">テキストテキストテキストテキストテキストテキストテキストテキストテキストテキストテキストテキスト</p></div>
  </div>
</section>

<section class="faq band-beige">
  <h2 class="sec-title" style="top:220px"><span class="en">Q&amp;A</span><span class="ja">よくある質問</span></h2>
  <ul class="faq-list">
    <li><p class="qa"><span class="mark q">Q</span>テキストテキストテキストテキストテキストテキストテキストテキストテキストテキスト</p><p class="qa"><span class="mark a">A</span>テキストテキストテキストテキストテキストテキストテキストテキストテキストテキスト</p></li>
    <li><p class="qa"><span class="mark q">Q</span>テキストテキストテキストテキストテキストテキストテキストテキストテキストテキスト</p><p class="qa"><span class="mark a">A</span>テキストテキストテキストテキストテキストテキストテキストテキストテキストテキスト</p></li>
    <li><p class="qa"><span class="mark q">Q</span>テキストテキストテキストテキストテキストテキストテキストテキストテキストテキスト</p><p class="qa"><span class="mark a">A</span>テキストテキストテキストテキストテキストテキストテキストテキストテキストテキスト</p></li>
  </ul>
</section>

<section class="contact">
  <a class="contact-btn" href="#">お問い合わせはこちら</a>
</section>
<div class="tree" role="img" aria-label="大きな緑の木のイラスト" style="background:radial-gradient(ellipse 60% 40% at 55% 35%,#3fa04f 0%,#2f9148 70%,transparent 72%),linear-gradient(to top,#2f9148 0,#2f9148 6%,transparent 6%)"></div>

<footer class="site-footer">
  <div class="foot-links">
    <span>Home</span>|<span>弊社の強み</span>|<span>事業案内</span>|<span>加工事例・商品紹介</span>|<span>お知らせ</span>|<span>よくある質問</span>|<span>お問い合わせ</span><br>
    <span>会社概要</span>|<span>アクセス</span>|<span>プライバシーポリシー</span>|<span>サイトマップ</span>
  </div>
  <div class="foot-brand"><span class="brand-dot"></span>株式会社 モリサト</div>
  <div class="foot-base"></div>
</footer>
</body>
</html>
```